" A consultoria tributária (também denominada consultoria fiscal) é um leque de atividades voltadas às questões que demandam análise específica dos temas que geram tributos ou obrigações fiscais, numa empresa. "

```html
<!DOCTYPE html>
<html lang="pt-BR">
<head>
<meta charset="UTF-8">
<title>LMR Consultoria Tributária – Blocos de Anotação</title>
<link rel="stylesheet" href="https://fonts.googleapis.com/css2?family=Cinzel:wght@500&family=Lato:wght@400;700&display=swap">
<style>
  :root {
    --page-bg: #ececec;
    --pad-black: #121212;
    --pad-black-soft: #2a2a2a;
    --pad-white: #ffffff;
    --ink-dark: #2b2b2b;
    --ink-muted: #6d6d6d;
    --gold: #c9a24a;
    --wire: #9a9a9a;
    --edge: #d9d9d9;
  }
  * { margin: 0; padding: 0; box-sizing: border-box; }
  html, body { width: 1200px; height: 1200px; overflow: hidden; }
  body {
    background: var(--page-bg);
    display: flex;
    align-items: center;
    justify-content: center;
    gap: 90px;
    font-family: "Lato", sans-serif;
  }
  .notepad {
    position: relative;
    width: 420px;
    height: 580px;
    border-radius: 6px;
    box-shadow: 0 10px 30px rgba(0,0,0,0.12), 0 2px 0 var(--edge);
  }
  .notepad--cover {
    background: linear-gradient(160deg, var(--pad-black-soft) 0%, var(--pad-black) 55%);
  }
  .notepad--sheet { background: var(--pad-white); }
  .spiral {
    position: absolute;
    top: -14px;
    left: 24px;
    width: 372px;
    height: 40px;
  }
  .brand {
    display: flex;
    align-items: center;
    gap: 12px;
  }
  .brand__dot {
    width: 30px;
    height: 30px;
    border-radius: 50%;
    background: var(--gold);
    flex-shrink: 0;
  }
  .brand__name {
    font-family: "Cinzel", serif;
    font-weight: 500;
    letter-spacing: 2px;
  }
  .brand__tagline {
    font-size: 9px;
    letter-spacing: 1.5px;
    text-transform: uppercase;
  }
  .notepad--cover .brand {
    position: absolute;
    top: 250px;
    left: 0;
    right: 0;
    justify-content: center;
  }
  .notepad--cover .brand__name { color: #ffffff; font-size: 48px; }
  .notepad--cover .brand__tagline {
    position: absolute;
    top: 312px;
    left: 0;
    right: 0;
    text-align: center;
    color: #bdbdbd;
  }
  .notepad--sheet .brand {
    position: absolute;
    top: 58px;
    left: 34px;
  }
  .notepad--sheet .brand__dot { width: 20px; height: 20px; }
  .notepad--sheet .brand__name { color: var(--ink-dark); font-size: 28px; }
  .notepad--sheet .brand__tagline {
    position: absolute;
    top: 96px;
    left: 66px;
    color: var(--ink-muted);
    font-size: 7px;
  }
  .contact-bar {
    position: absolute;
    left: 24px;
    right: 24px;
    bottom: 22px;
    display: flex;
    justify-content: space-between;
    border-top: 1px solid var(--edge);
    padding-top: 10px;
    font-size: 10px;
    color: var(--ink-muted);
  }
  .contact-bar__item { display: flex; align-items: center; gap: 5px; }
  .contact-bar__item svg { width: 10px; height: 10px; fill: var(--gold); }
</style>
</head>
<body>

  <section class="notepad notepad--cover">
    <svg class="spiral" viewBox="0 0 372 40" aria-hidden="true">
      <g fill="none" stroke="var(--wire)" stroke-width="3" stroke-linecap="round">
        <path d="M6 30 V8 a4 4 0 0 1 8 0 V30"/><path d="M34 30 V8 a4 4 0 0 1 8 0 V30"/>
        <path d="M62 30 V8 a4 4 0 0 1 8 0 V30"/><path d="M90 30 V8 a4 4 0 0 1 8 0 V30"/>
        <path d="M118 30 V8 a4 4 0 0 1 8 0 V30"/><path d="M146 30 V8 a4 4 0 0 1 8 0 V30"/>
        <path d="M174 30 V8 a4 4 0 0 1 8 0 V30"/><path d="M202 30 V8 a4 4 0 0 1 8 0 V30"/>
        <path d="M230 30 V8 a4 4 0 0 1 8 0 V30"/><path d="M258 30 V8 a4 4 0 0 1 8 0 V30"/>
        <path d="M286 30 V8 a4 4 0 0 1 8 0 V30"/><path d="M314 30 V8 a4 4 0 0 1 8 0 V30"/>
        <path d="M342 30 V8 a4 4 0 0 1 8 0 V30"/>
      </g>
    </svg>
    <div class="brand">
      <span class="brand__dot"></span>
      <span class="brand__name">LMR</span>
    </div>
    <p class="brand__tagline">Consultoria Tributária</p>
  </section>

  <section class="notepad notepad--sheet">
    <svg class="spiral" viewBox="0 0 372 40" aria-hidden="true">
      <g fill="none" stroke="var(--wire)" stroke-width="3" stroke-linecap="round">
        <path d="M6 30 V8 a4 4 0 0 1 8 0 V30"/><path d="M34 30 V8 a4 4 0 0 1 8 0 V30"/>
        <path d="M62 30 V8 a4 4 0 0 1 8 0 V30"/><path d="M90 30 V8 a4 4 0 0 1 8 0 V30"/>
        <path d="M118 30 V8 a4 4 0 0 1 8 0 V30"/><path d="M146 30 V8 a4 4 0 0 1 8 0 V30"/>
        <path d="M174 30 V8 a4 4 0 0 1 8 0 V30"/><path d="M202 30 V8 a4 4 0 0 1 8 0 V30"/>
        <path d="M230 30 V8 a4 4 0 0 1 8 0 V30"/><path d="M258 30 V8 a4 4 0 0 1 8 0 V30"/>
        <path d="M286 30 V8 a4 4 0 0 1 8 0 V30"/><path d="M314 30 V8 a4 4 0 0 1 8 0 V30"/>
        <path d="M342 30 V8 a4 4 0 0 1 8 0 V30"/>
      </g>
    </svg>
    <div class="brand">
      <span class="brand__dot"></span>
      <span class="brand__name">LMR</span>
    </div>
    <p class="brand__tagline">Consultoria Tributária</p>

    <footer class="contact-bar">
      <span class="contact-bar__item">
        <svg viewBox="0 0 10 10"><path d="M2 0 L4 2.5 L3 3.8 Q4.5 6 6.2 7 L7.5 6 L10 8 L8.5 10 Q2 8.5 0 1.5 Z"/></svg>
        (11) 4020-7315
      </span>
      <span class="contact-bar__item">
        <svg viewBox="0 0 10 10"><path d="M0 2 H10 V8 H0 Z M0 2 L5 5.5 L10 2" /></svg>
        contato@lmrfiscal.com.br
      </span>
      <span class="contact-bar__item">
        <svg viewBox="0 0 10 10"><circle cx="5" cy="5" r="5"/></svg>
        www.lmrfiscal.com.br
      </span>
    </footer>
  </section>

</body>
</html>
```